Upgrade of Lumora chocolate toffee design

Lumora Choc toffee is a very popular sweet on the Zimbabwean market, we want to spruce up the design to make it more attractive. Attached is the existing design. The new design must be not more than six colours and for printing on photogravure which is a print technology for flexible packaging. The design should empahsise the chocolate flavour but we need to move away from the words rich and creamy. The design is aimed at the younger consumer and should look eyecatching
Updates

Target Market(s)

Middle income Zimbabwean consumers, mainly younger

Requirements
Must have
• Lumora logo in the same format but with colour changes allowed. Also must have a clear window on the front of the pack through which the sweets can be seen

```html
<!DOCTYPE html>
<html lang="en">
<head>
<meta charset="utf-8">
<title>Lumora Chocolate Toffees – Pack Front</title>
<link rel="stylesheet" href="https://fonts.googleapis.com/css2?family=Yesteryear&family=Oswald:wght@500&family=Roboto+Condensed:wght@700&display=swap">
<style>
  :root {
    --backdrop: #e4e4e6;
    --choc-dark: #3a1d0e;
    --choc-mid: #7a4322;
    --choc-light: #b9773f;
    --yellow: #f3c316;
    --yellow-deep: #e39a0c;
    --window: #c9c9cb;
    --window-light: #dadadc;
    --cream: #f6ecc4;
    --toffee: #c46a22;
    --toffee-light: #e59a4e;
    --ink: #141414;
    --brown-text: #5a2b12;
  }
  * { margin: 0; padding: 0; box-sizing: border-box; }
  html, body { width: 1200px; height: 1198px; overflow: hidden; }
  body { background: var(--backdrop); position: relative; font-family: "Roboto Condensed", sans-serif; }

  .pack { position: absolute; left: 224px; top: 64px; width: 760px; height: 1072px; }
  .pack-art { position: absolute; inset: 0; }

  .brand-name {
    position: absolute; left: 0; right: 0; top: 112px;
    text-align: center;
    font-family: "Yesteryear", cursive; font-size: 124px; line-height: 1;
    color: #ffffff;
  }
  .product-name {
    position: absolute; left: 108px; top: 330px;
    font-family: "Yesteryear", cursive; font-size: 82px; line-height: 1;
    color: var(--cream);
    transform: rotate(-7deg); transform-origin: left center;
    text-shadow: 0 3px 0 var(--choc-dark);
  }
  .claim {
    position: absolute; left: 224px; top: 632px;
    font-family: "Yesteryear", cursive; font-size: 70px; line-height: 1;
    color: var(--cream);
    transform: rotate(-17deg); transform-origin: left center;
    text-shadow: 0 3px 0 var(--toffee);
  }
  .weight-badge {
    position: absolute; left: 104px; top: 766px; width: 136px; height: 136px;
    border-radius: 50%;
    background: radial-gradient(circle, var(--cream) 60%, var(--yellow) 62%, var(--yellow-deep) 100%);
    display: flex; flex-direction: column; align-items: center; justify-content: center;
    color: var(--brown-text); text-align: center;
  }
  .weight-badge .badge-type { font-family: "Yesteryear", cursive; font-size: 25px; line-height: 1.05; }
  .weight-badge .badge-weight { font-family: "Roboto Condensed", sans-serif; font-weight: 700; font-size: 26px; margin-top: 4px; }

  .window-note {
    position: absolute; left: 76px; top: 574px;
    font-family: "Oswald", sans-serif; font-weight: 500; font-size: 26px; line-height: 1.15;
    color: var(--ink); text-align: center; width: 180px;
  }
  .window-note-line { position: absolute; left: 152px; top: 645px; width: 216px; height: 1px; background: var(--ink); }
</style>
</head>
<body>
  <div class="pack">
    <svg class="pack-art" width="760" height="1072" viewBox="0 0 760 1072">
      <defs>
        <radialGradient id="chocSwirl" cx="0.5" cy="0.35" r="0.7">
          <stop offset="0" stop-color="#b9773f"/>
          <stop offset="0.55" stop-color="#7a4322"/>
          <stop offset="1" stop-color="#3a1d0e"/>
        </radialGradient>
        <linearGradient id="windowTone" x1="0" y1="0" x2="1" y2="1">
          <stop offset="0" stop-color="#dadadc"/>
          <stop offset="1" stop-color="#c9c9cb"/>
        </linearGradient>
        <radialGradient id="toffeeTone" cx="0.5" cy="0.5" r="0.55">
          <stop offset="0" stop-color="#e59a4e"/>
          <stop offset="0.6" stop-color="#c46a22"/>
          <stop offset="0.85" stop-color="#e8c48e"/>
          <stop offset="1" stop-color="#f6ecc4"/>
        </radialGradient>
      </defs>
      <rect class="window-area" x="0" y="0" width="760" height="1072" fill="url(#windowTone)"/>
      <path class="wave-band" d="M0 410 C200 440 420 490 760 370 L760 490 C430 590 210 560 0 530 Z" fill="var(--yellow)"/>
      <path class="choc-top" role="img" aria-label="Swirling melted chocolate illustration"
            d="M0 0 H760 V390 C420 490 200 460 0 430 Z" fill="url(#chocSwirl)"/>
      <ellipse class="toffee-art" role="img" aria-label="Chocolate toffee pieces on a milk splash"
               cx="470" cy="870" rx="220" ry="168" fill="url(#toffeeTone)"/>
    </svg>
    <div class="brand-name">Lumora</div>
    <div class="product-name">Chocolate Toffees</div>
    <div class="claim">Extra Chocolatey</div>
    <div class="weight-badge">
      <span class="badge-type">Glucose<br>Sweets</span>
      <span class="badge-weight">75 g</span>
    </div>
  </div>
  <div class="window-note">TRANSPARENT<br>AREA</div>
  <div class="window-note-line"></div>
</body>
</html>
```